Accommodation in an Executive Apartment for rent could be a Bed and breakfast,

Currently have a website and like the overall look but it needs revamping and want to add an instant booking button, which I would do later as the unit has a channel manager. Also want to be able to post blogs, etc. Need it to be viewed well on smart phones/tablets. all information related to this unit is on the current site which is www.lorvenstaysmirrabrook.com.au if you would view websites similar to staywell.example and roamtrip.example Must be able to be coded in Wordpress

The current design is done in Wordpress so would want this functionality in any new design.

Target Market(s)

Workers at Quorran precinct, Canberra. Workers at Halvern centre Deakin, Workers at Marlow Peter Tenby Hospital, Workers at Brindlewood Hospital, Public Servants Woden, Workers in Deakin ACT

Industry/Entity Type

Accommodation

Number of Pages Required

5+ page

Font styles to use
Sans Serif

Colors
ec1f27

Requirements
Must have
• Must have a classy look about it. Less clicks through the better. Not to wordy. Hard hitting points,
Nice to have
• Would like to retain the same colour theme and look
Should not have
• anything tacky

```html
<!DOCTYPE html>
<html lang="en">
<head>
<meta charset="utf-8">
<title>Lorven executive bed &amp; breakfast</title>
<link href="https://fonts.googleapis.com/css2?family=Lato:ital,wght@0,400;0,700;1,400&family=Oswald:wght@500&display=swap" rel="stylesheet">
<style>
:root{
  --red:#ec1f27;
  --maroon:#7c1a1f;
  --maroon-dark:#5e1217;
  --ink:#222;
  --text:#555;
  --muted:#888;
  --panel:#efefef;
  --footer:#27282a;
  --footer-deep:#222325;
  --line:#e3e3e3;
}
*{margin:0;padding:0;box-sizing:border-box}
html,body{width:714px;height:1200px;overflow:hidden;background:#fff}
body{position:relative;font-family:'Lato',sans-serif;color:var(--text)}
.abs{position:absolute}

/* header */
.site-header{left:0;top:0;width:714px;height:67px;background:linear-gradient(180deg,var(--maroon),var(--maroon-dark))}
.brand{left:44px;top:20px;color:#fff;font-size:19px;font-weight:400;letter-spacing:.2px}
.contact-top{right:44px;top:16px;text-align:right;color:#fff}
.contact-top .addr{font-size:10.5px}
.contact-top .phone{font-size:14px;margin-top:3px;display:flex;align-items:center;justify-content:flex-end;gap:5px}

/* nav */
.main-nav{left:0;top:67px;width:714px;height:31px;background:linear-gradient(180deg,#fafafa,#dedede);border-bottom:1px solid #c9c9c9}
.main-nav a{position:absolute;top:0;height:31px;line-height:31px;font-size:7.5px;color:#333;text-decoration:none;text-transform:uppercase}
.main-nav a.active{background:var(--maroon);color:#fff;width:59px;text-align:center}

/* hero */
.hero{left:0;top:98px;width:714px;height:307px;background:linear-gradient(100deg,#8c7b6c 0%,#cfc8bf 30%,#e9e7e3 55%,#d8d2cb 80%,#a9a097 100%)}
.hero-badge{left:100px;top:174px;width:154px;height:154px;border-radius:50%;background:rgba(255,255,255,.55);padding:6px}
.hero-badge .inner{width:100%;height:100%;border-radius:50%;background:#f7f6ef;text-align:center;padding-top:28px;color:#111}
.hero-badge .big{font-family:'Oswald',sans-serif;font-size:32px;line-height:32px;letter-spacing:-1px}
.hero-badge .amp{font-size:20px;font-style:italic;margin:3px 0;display:flex;align-items:center;justify-content:center;gap:8px}
.hero-badge .amp i{display:block;width:30px;height:1px;background:#999}
.hero-badge .small{font-family:'Oswald',sans-serif;font-size:18px;letter-spacing:-.5px}
.hero-copy{left:282px;top:210px;width:290px;font-size:9.2px;line-height:14.4px;font-style:italic;color:#222}
.btn{display:block;background:var(--red);color:#fff;text-align:center;text-transform:uppercase;text-decoration:none}
.hero-btn{left:282px;top:272px;width:120px;height:28px;line-height:28px;font-size:9.5px;letter-spacing:.6px;border-radius:2px}
.slider-dots{left:325px;top:382px;display:flex;align-items:center;gap:5px}
.dot{width:7px;height:7px;border-radius:50%;border:1px solid #333}
.dot.on{background:var(--red);border-color:var(--red)}

/* welcome */
.section-title{width:714px;left:0;text-align:center;color:var(--ink);font-size:15px;letter-spacing:.2px}
.title-rule{left:339px;width:36px;height:2px;background:var(--red)}
.welcome-copy{left:122px;top:478px;width:470px;text-align:center;font-size:7.8px;line-height:13px}

/* rooms */
.room{width:160px;top:538px}
.room-head{height:34px;line-height:34px;background:var(--panel);text-align:center;color:var(--red);font-size:11.5px;letter-spacing:.5px;text-transform:uppercase}
.room-photo{position:relative;height:127px}
.room-photo .arr{position:absolute;top:55px;width:12px;height:16px;background:rgba(0,0,0,.25)}
.amenities{display:flex;justify-content:center;gap:7px;margin-top:9px}
.room-text{margin-top:9px;text-align:center;font-size:7.6px;line-height:12px;padding:0 2px}
.room-btn{margin:10px auto 0;width:76px;height:20px;line-height:20px;font-size:7.5px;letter-spacing:.4px}
.divider{left:44px;top:828px;width:626px;height:1px;background:var(--line)}

/* blog */
.post{top:887px;width:250px}
.avatar{position:absolute;left:0;top:0;width:48px;height:48px}
.post p{position:absolute;left:58px;top:-2px;width:192px;font-size:8.3px;line-height:13.3px;text-align:justify}
.post .by{position:absolute;right:0;top:50px;color:var(--red);font-size:8.3px}

/* footer */
.site-footer{left:0;top:978px;width:714px;height:222px;background:var(--footer)}
.footer-bottom{left:0;top:1158px;width:714px;height:42px;background:var(--footer-deep);text-align:center;line-height:42px;font-size:7.5px;color:#aaa}
.footer-brand{left:44px;top:1007px;color:#ddd;font-size:14px}
.footer-about{left:45px;top:1037px;width:190px;font-size:8.3px;line-height:13.3px;color:#aaa;text-align:justify}
.socials{left:44px;top:1096px;display:flex;gap:15px}
.socials span{width:15px;height:15px;border:1.3px solid #ccc;border-radius:3px}
.footer-title{top:1005px;color:#eee;font-size:12.5px;letter-spacing:1px;text-transform:uppercase}
.explore{left:276px;top:1030px;list-style:none}
.explore li{font-size:6.8px;color:#bbb;height:16.5px;text-transform:uppercase}
.field{border:1px solid #bbb;color:#aaa;font-size:7.5px;display:flex;align-items:center;gap:5px;padding-left:10px}
.submit{left:579px;top:1107px;width:91px;height:24px;line-height:24px;font-size:8px;letter-spacing:.5px}
</style>
</head>
<body>

<header class="abs site-header">
  <div class="abs brand">Lorven executive bed &amp; breakfast</div>
  <div class="abs contact-top">
    <div class="addr">Ashgrove Crescent Mirrabrook</div>
    <div class="phone">
      <svg width="11" height="11" viewBox="0 0 24 24" fill="none" stroke="#fff" stroke-width="2"><path d="M5 3h4l2 5-2.5 1.5a11 11 0 0 0 6 6L16 13l5 2v4a2 2 0 0 1-2 2A17 17 0 0 1 3 5a2 2 0 0 1 2-2z"/></svg>
      02 5550 1842
    </div>
  </div>
</header>

<nav class="abs main-nav">
  <a class="active" style="left:44px">Home</a>
  <a style="left:121px">B&amp;B Accommodation</a>
  <a style="left:237px">Gallery</a>
  <a style="left:300px">What's nearby</a>
  <a style="left:390px">Guest book</a>
  <a style="left:472px">Useful links</a>
  <a style="left:552px">Contact us</a>
</nav>

<section class="abs hero" role="img" aria-label="Softly blurred photo of a bright hotel bedroom with white bedding and curtains"></section>
<div class="abs hero-badge">
  <div class="inner">
    <div class="big">BED</div>
    <div class="amp"><i></i>&amp;<i></i></div>
    <div class="small">BREAKFAST</div>
  </div>
</div>
<p class="abs hero-copy">Magna aliqua Ut enim ad minim veniam, quis nostrud exercitation ullamco laboris nisi ut aliquip ex ea commodo consequat. Duis aute irure dolor in reprehenderit in voluptate</p>
<a class="abs btn hero-btn">Instant booking</a>
<div class="abs slider-dots">
  <svg width="12" height="12" viewBox="0 0 12 12"><circle cx="6" cy="6" r="6" fill="#222"/><path d="M7 3L4 6l3 3" stroke="#fff" stroke-width="1.5" fill="none"/></svg>
  <span class="dot"></span><span class="dot on"></span><span class="dot"></span>
  <svg width="12" height="12" viewBox="0 0 12 12"><circle cx="6" cy="6" r="6" fill="#222"/><path d="M5 3l3 3-3 3" stroke="#fff" stroke-width="1.5" fill="none"/></svg>
</div>

<h2 class="abs section-title" style="top:443px;font-weight:400">WELCOME TO OUR SITE</h2>
<div class="abs title-rule" style="top:464px"></div>
<p class="abs welcome-copy">Lorem ipsum dolor sit amet, consectetur adipiscing elit, sed do eiusmod tempor incididunt ut labore et dolore magna aliqua. Ut enim ad minim veniam, quis nostrud exercitation ullamco laboris nisi ut aliquip ex ea commodo consequat. Duis aute irure dolor in reprehenderit in voluptate velit esse cillum dolore eu fugiat nulla pariatur.</p>

<article class="abs room" style="left:98px">
  <div class="room-head">Single room</div>
  <div class="room-photo" role="img" aria-label="Photo of a single room lounge with sofas and a coffee table" style="background:linear-gradient(135deg,#8a6a3e,#d8c6a0 50%,#6e4e2e)"><span class="arr" style="left:0"></span><span class="arr" style="right:0"></span></div>
  <div class="amenities">
    <svg width="110" height="14" viewBox="0 0 110 14" fill="#aaa"><path d="M2 2l8 8M6 12h6" stroke="#aaa" stroke-width="2"/><rect x="22" y="1" width="2" height="12"/><rect x="26" y="1" width="2" height="12"/><rect x="38" y="2" width="12" height="8"/><rect x="42" y="11" width="4" height="2"/><rect x="60" y="1" width="10" height="12" rx="1"/><text x="80" y="13" font-family="Lato" font-weight="700" font-size="15">P</text><rect x="96" y="1" width="12" height="10"/><rect x="95" y="11" width="14" height="2"/></svg>
  </div>
  <p class="room-text">Lorem ipsum dolor sit amet, consectetur adipiscing elit, sed do eiusmod tempor incididunt ut labore dolore.</p>
  <a class="btn room-btn">Book now</a>
</article>

<article class="abs room" style="left:277px">
  <div class="room-head">Double room</div>
  <div class="room-photo" role="img" aria-label="Photo of a double room living area with television and dining table" style="background:linear-gradient(135deg,#b08a4e,#e8dcc0 50%,#8a6a3a)"><span class="arr" style="left:0"></span><span class="arr" style="right:0"></span></div>
  <div class="amenities">
    <svg width="110" height="14" viewBox="0 0 110 14" fill="#aaa"><path d="M2 2l8 8M6 12h6" stroke="#aaa" stroke-width="2"/><rect x="22" y="1" width="2" height="12"/><rect x="26" y="1" width="2" height="12"/><rect x="38" y="2" width="12" height="8"/><rect x="42" y="11" width="4" height="2"/><rect x="60" y="1" width="10" height="12" rx="1"/><text x="80" y="13" font-family="Lato" font-weight="700" font-size="15">P</text><rect x="96" y="1" width="12" height="10"/><rect x="95" y="11" width="14" height="2"/></svg>
  </div>
  <p class="room-text">Lorem ipsum dolor sit amet, consectetur adipiscing elit, sed do eiusmod tempor incididunt ut labore dolore.</p>
  <a class="btn room-btn">Book now</a>
</article>

<article class="abs room" style="left:456px">
  <div class="room-head">Luxury suite</div>
  <div class="room-photo" role="img" aria-label="Photo of a luxury suite bathroom with glass shower and vanity" style="background:linear-gradient(90deg,#a9b3b5,#e6e8e6 50%,#f4f4f2)"><span class="arr" style="left:0"></span><span class="arr" style="right:0"></span></div>
  <div class="amenities">
    <svg width="110" height="14" viewBox="0 0 110 14" fill="#aaa"><path d="M2 2l8 8M6 12h6" stroke="#aaa" stroke-width="2"/><rect x="22" y="1" width="2" height="12"/><rect x="26" y="1" width="2" height="12"/><rect x="38" y="2" width="12" height="8"/><rect x="42" y="11" width="4" height="2"/><rect x="60" y="1" width="10" height="12" rx="1"/><text x="80" y="13" font-family="Lato" font-weight="700" font-size="15">P</text><rect x="96" y="1" width="12" height="10"/><rect x="95" y="11" width="14" height="2"/></svg>
  </div>
  <p class="room-text">Lorem ipsum dolor sit amet, consectetur adipiscing elit, sed do eiusmod tempor incididunt ut labore dolore.</p>
  <a class="btn room-btn">Book now</a>
</article>

<div class="abs divider"></div>

<h2 class="abs section-title" style="top:854px;font-weight:400">BLOG &nbsp;POST</h2>

<article class="abs post" style="left:98px">
  <div class="avatar" role="img" aria-label="Portrait photo of the guest" style="background:linear-gradient(160deg,#c9c9c9,#6a5a50)"></div>
  <p>Lorem ipsum dolor sit du amet, consectetur adipiscing elit, sed do eiusmod tempor incide ut labore et dolore magna aliqua.</p>
  <span class="by">Daniel R., Leeds</span>
</article>
<article class="abs post" style="left:367px">
  <div class="avatar" role="img" aria-label="Portrait photo of the guest" style="background:linear-gradient(160deg,#d8cbbf,#9a7a5a)"></div>
  <p>Nemo enim ipsam voluptatem quia voluptas sit aspernatur aut odit aut dues fugit, sed quia consequuntur magni dolores.</p>
  <span class="by">Harriet P., Bristol</span>
</article>

<footer class="abs site-footer"></footer>
<div class="abs footer-brand">Lorven executive bed &amp; breakfast</div>
<p class="abs footer-about">Lorem ipsum dolor sit du amet, consectetur adipiscing elit, sed do eiusmod tempor incide ut labore et dolore magna aliqua.</p>
<div class="abs socials"><span></span><span></span><span></span><span></span></div>

<h3 class="abs footer-title" style="left:276px;font-weight:400">Explore</h3>
<ul class="abs explore">
  <li>Home</li><li>B&amp;B Accommodation</li><li>Gallery</li><li>What's nearby</li><li>Guest book</li><li>Contact us</li>
</ul>

<h3 class="abs footer-title" style="left:402px;font-weight:400">Contact info</h3>
<div class="abs field" style="left:402px;top:1031px;width:130px;height:20px">
  <svg width="8" height="8" viewBox="0 0 10 10" fill="#ccc"><circle cx="5" cy="3" r="2.5"/><path d="M0 10a5 4 0 0 1 10 0z"/></svg>Name
</div>
<div class="abs field" style="left:541px;top:1031px;width:129px;height:20px">
  <svg width="9" height="8" viewBox="0 0 12 9" fill="none" stroke="#ccc"><rect x=".5" y=".5" width="11" height="8"/><path d="M.5 .5l5.5 4 5.5-4"/></svg>Email
</div>
<div class="abs field" style="left:402px;top:1059px;width:268px;height:39px;align-items:flex-start;padding-top:9px">
  <svg width="9" height="8" viewBox="0 0 12 10" fill="#ccc"><ellipse cx="6" cy="4" rx="6" ry="4"/><path d="M2 7l-1 3 4-2z"/></svg>Leave Message
</div>
<a class="abs btn submit">Submit here</a>

<div class="abs footer-bottom">Copyright 2015, Yoursite, All Right Reserved</div>

</body>
</html>
```